Request for Business Card Design

Hi. My name is Marlena, I am looking for a new business card design for my company, Quillbrook Sensing Systems, LLC. I really like the design you did for Tavel Harvest and was hoping you could do something similar using our full logo and our mark. I am also open to any raised texture design using our mark. I have attached our full logo, which would need to be somewhere on the card, as well as the mark in both outline and full form, as well as our brand colors / guide. The card does not have to be white, as long as our logo and mark appear. I actually like darker colored business cards more, but am open to all options. If you are interested in working with me, please let me know. We would also take the business card design into letterhead design if you can do that.

```html
<!DOCTYPE html>
<html lang="en">
<head>
<meta charset="utf-8">
<title>Quillbrook Sensing Systems – Business Card</title>
<link rel="stylesheet" href="https://fonts.googleapis.com/css2?family=Open+Sans:wght@400;600;700&display=swap">
<style>
  :root {
    --stage: #222223;
    --card: #3d3d3f;
    --card-deep: #2c2c2e;
    --brand-blue: #1a9cc9;
    --white: #ffffff;
    --text-soft: #e9e9ea;
    --ring: rgba(26, 156, 201, 0.16);
  }
  * { box-sizing: border-box; margin: 0; padding: 0; }
  html, body {
    width: 1200px; height: 780px; overflow: hidden;
    background: var(--stage);
    font-family: "Open Sans", Arial, sans-serif;
  }
  .stage {
    position: relative; width: 1200px; height: 780px;
    display: flex; align-items: center; justify-content: center; gap: 40px;
  }
  .card {
    position: relative; width: 560px; height: 320px;
    background: var(--card);
    border-radius: 18px;
    border-bottom: 5px solid var(--brand-blue);
    overflow: hidden;
  }

  /* Back side */
  .card-back { display: flex; align-items: center; justify-content: center; }
  .back-lockup { display: flex; align-items: center; gap: 16px; }
  .back-dot { width: 46px; height: 46px; border-radius: 50%; background: var(--card-deep); }
  .back-name {
    font-weight: 700; font-size: 26px; letter-spacing: 3px; line-height: 1.15;
    color: var(--card-deep); text-transform: uppercase;
  }

  /* Front side */
  .front-ring {
    position: absolute; right: 40px; top: 40px; width: 250px; height: 250px;
    border-radius: 50%; border: 3px solid var(--ring);
  }
  .front-lockup {
    position: absolute; left: 30px; top: 32px;
    display: flex; align-items: center; gap: 12px;
  }
  .front-dot { width: 34px; height: 34px; border-radius: 50%; background: var(--brand-blue); }
  .front-name {
    font-weight: 700; font-size: 17px; letter-spacing: 2px; line-height: 1.2;
    color: var(--white); text-transform: uppercase;
  }
  .address {
    position: absolute; left: 78px; top: 112px;
    font-size: 13px; line-height: 1.4; color: var(--text-soft);
  }
  .contact-list {
    position: absolute; left: 78px; top: 162px; list-style: none;
    font-size: 12.5px; line-height: 1.55; color: var(--text-soft);
  }
  .contact-list li { display: flex; align-items: center; gap: 8px; }
  .contact-list svg { width: 12px; height: 12px; flex: none; fill: var(--brand-blue); }
  .person {
    position: absolute; right: 34px; top: 150px; text-align: right;
  }
  .person-name { font-weight: 700; font-size: 34px; color: var(--brand-blue); line-height: 1; }
  .person-role { font-weight: 600; font-size: 14px; color: var(--white); margin-top: 2px; }
  .bands { position: absolute; left: 0; bottom: 0; width: 560px; height: 100px; }
</style>
</head>
<body>
<main class="stage">

  <section class="card card-back" aria-label="Card back">
    <div class="back-lockup">
      <span class="back-dot"></span>
      <p class="back-name">Quillbrook<br>Sensing Systems</p>
    </div>
  </section>

  <section class="card card-front" aria-label="Card front">
    <div class="front-ring" role="img" aria-label="Faint large brand mark decoration"></div>

    <div class="front-lockup">
      <span class="front-dot"></span>
      <p class="front-name">Quillbrook<br>Sensing Systems</p>
    </div>

    <p class="address">1180 Meridian Park Drive<br>Halden, CO 80417</p>

    <ul class="contact-list">
      <li><svg viewBox="0 0 24 24"><path d="M6.6 10.8a15 15 0 0 0 6.6 6.6l2.2-2.2a1 1 0 0 1 1-.25 11 11 0 0 0 3.6.6 1 1 0 0 1 1 1V20a1 1 0 0 1-1 1A17 17 0 0 1 3 4a1 1 0 0 1 1-1h3.5a1 1 0 0 1 1 1 11 11 0 0 0 .6 3.6 1 1 0 0 1-.25 1z"/></svg>+001 555 210 4482</li>
      <li><svg viewBox="0 0 24 24"><path d="M6 2h10v6H6zM3 9h18v11H3zm4 3v2h2v-2zm4 0v2h2v-2zm4 0v2h2v-2zm-8 4v2h2v-2zm4 0v2h2v-2z"/></svg>+001 555 210 4490</li>
      <li><svg viewBox="0 0 24 24"><path d="M12 2a10 10 0 1 0 0 20 10 10 0 0 0 0-20zm0 2c1 1.3 1.8 3 2.2 5H9.8c.4-2 1.2-3.7 2.2-5zM4.3 14a8 8 0 0 1 0-4h3.4a17 17 0 0 0 0 4zm5.5 0a15 15 0 0 1 0-4h4.4a15 15 0 0 1 0 4zm6.5 0a17 17 0 0 0 0-4h3.4a8 8 0 0 1 0 4zM12 20c-1-1.3-1.8-3-2.2-5h4.4c-.4 2-1.2 3.7-2.2 5z"/></svg>www.quillbrooksensing.com</li>
      <li><svg viewBox="0 0 24 24"><path d="M2 5h20v14H2zm2 2v.5l8 5 8-5V7l-8 5z"/></svg>info@quillbrooksensing.com</li>
    </ul>

    <div class="person">
      <p class="person-name">Marlena</p>
      <p class="person-role">Director</p>
    </div>

    <svg class="bands" viewBox="0 0 560 100" preserveAspectRatio="none" aria-hidden="true">
      <polygon points="0,70 330,70 370,52 330,100 0,100" fill="var(--brand-blue)"/>
      <polygon points="0,86 300,86 290,100 0,100" fill="var(--card)"/>
      <polygon points="370,52 560,8 560,26 395,60" fill="var(--white)"/>
    </svg>
  </section>

</main>
</body>
</html>
```